Tablet App design for business management system

TaskOra is a business management system made especially for service based businesses (our subscribers). It enables systemising your service businesses. This can be used by diverse industries like automotive service, beauty (hair salons, nail spas), Spas, Chiropractor, acupuntcure, osteo, yoga studio, business coach, etc.

The UI of the app needs to be designed using flat and clean UI design trends that are currently prevailing for B2C apps. Even the sliding menu panel can be removed and alternative placement of this functionality can be suggested. The color palette used for the design should be limited (3-5 colours)

The Current UI screens are open to suggestions for change. For ease of management in minimum steps, consolidation of functionality on different screens can be suggested, accompanies by a rational reason with the objective of having a simple and straight forward user experience.

User should be able to move from one function to another (booking > view appointments > profile) in no more than 1 or max 2 gestures.

Target Market(s)

SME businesses that provide time based services

Industry/Entity Type

Business

Font styles to use
Sans Serif

Requirements
Must have
• The power point slides give a detailed account of the process flow and functionality that the app is to follow.
• Reference this slide to ensure that your final design must have all screens that are required to deliver the functionality.

```html
<!DOCTYPE html>
<html lang="en">
<head>
<meta charset="utf-8">
<title>TaskOra – Appointments &amp; Check In</title>
<link rel="stylesheet" href="https://fonts.googleapis.com/css2?family=Roboto:wght@400;500&display=swap">
<style>
  :root {
    --teal: #1bb3c8;
    --list-bg: #ececec;
    --card: #ffffff;
    --ink: #111111;
    --ink-soft: #4a4a4a;
    --muted: #8a8a8a;
    --deep-blue: #2a3c9e;
    --sea: #33bccb;
    --ok: #2fb84a;
    --wait: #f0b400;
    --late: #e8383d;
    --page: #e9ecef;
  }
  * { box-sizing: border-box; margin: 0; padding: 0; }
  html, body { width: 1200px; height: 943px; overflow: hidden; background: var(--page); font-family: "Roboto", sans-serif; }
  .screen { position: absolute; left: 0; top: 21px; width: 1200px; height: 900px; overflow: hidden; background: var(--list-bg); }

  .status-bar { position: absolute; left: 0; top: 0; width: 1200px; height: 26px; background: #000; color: #fff; font-size: 13px; display: flex; align-items: center; justify-content: space-between; padding: 0 10px; z-index: 3; }
  .status-left, .status-right { display: flex; align-items: center; gap: 6px; width: 200px; }
  .status-right { justify-content: flex-end; }
  .battery { width: 24px; height: 11px; border: 1px solid #fff; border-radius: 2px; padding: 1px; }
  .battery span { display: block; width: 100%; height: 100%; background: #fff; }

  .appointments { position: absolute; left: 0; top: 26px; width: 597px; height: 874px; background: var(--list-bg); }
  .app-header { height: 52px; background: var(--teal); color: #fff; display: flex; align-items: center; justify-content: center; font-size: 20px; font-weight: 500; position: relative; }
  .menu-btn { position: absolute; left: 14px; top: 16px; }
  .add-btn { position: absolute; right: 12px; top: 12px; }
  .consultant-filter { position: absolute; left: 8px; top: 63px; width: 582px; height: 46px; background: var(--card); display: flex; align-items: center; justify-content: space-between; padding: 0 18px 0 12px; font-size: 18px; color: var(--ink); box-shadow: 0 1px 2px rgba(0,0,0,.12); }
  .caret { width: 0; height: 0; border-left: 5px solid transparent; border-right: 5px solid transparent; border-top: 6px solid #666; }

  .time-label { position: absolute; left: 8px; font-size: 17px; color: var(--muted); }
  .appt-card { position: absolute; left: 94px; width: 503px; height: 115px; background: var(--card); }

  .avatar { position: absolute; left: 16px; top: 20px; width: 59px; height: 59px; border-radius: 50%; }
  .person-name { position: absolute; left: 92px; top: 24px; font-size: 20px; font-weight: 500; color: var(--ink); white-space: nowrap; }
  .services { position: absolute; left: 92px; top: 50px; font-size: 16px; color: var(--ink-soft); white-space: nowrap; }
  .consultant { position: absolute; left: 92px; top: 83px; font-size: 16px; color: var(--ink-soft); display: flex; align-items: center; gap: 8px; white-space: nowrap; }
  .dot { width: 18px; height: 18px; border-radius: 50%; display: inline-flex; align-items: center; justify-content: center; }
  .dot.ok { background: var(--ok); } .dot.wait { background: var(--wait); } .dot.late { background: var(--late); }

  .check-in { position: absolute; left: 597px; top: 26px; width: 603px; height: 874px; background: linear-gradient(180deg, var(--deep-blue) 0%, #2f68b8 40%, var(--sea) 100%); }
  .check-header { height: 52px; color: #fff; font-size: 20px; font-weight: 500; display: flex; align-items: center; justify-content: center; }
  .search-bar { position: absolute; left: 12px; top: 60px; width: 579px; height: 46px; background: rgba(20,35,120,.45); color: #fff; font-size: 18px; display: flex; align-items: center; justify-content: center; gap: 10px; }
  .checkin-card { position: absolute; left: 51px; width: 492px; height: 116px; background: var(--card); box-shadow: 0 2px 4px rgba(0,0,0,.2); }
</style>
</head>
<body>
<main class="screen">
  <div class="status-bar">
    <div class="status-left">Tablet
      <svg width="14" height="11" viewBox="0 0 14 11"><path d="M7 10 L9 7.5 A3 3 0 0 0 5 7.5 Z M2.6 5 A6.5 6.5 0 0 1 11.4 5 L10.2 6.3 A4.8 4.8 0 0 0 3.8 6.3 Z M0.3 2.6 A9.8 9.8 0 0 1 13.7 2.6 L12.5 3.9 A8 8 0 0 0 1.5 3.9 Z" fill="#fff"/></svg>
    </div>
    <div>4:21 PM</div>
    <div class="status-right">
      <svg width="8" height="12" viewBox="0 0 8 12"><path d="M1 3 L7 8.5 L4 11 V1 L7 3.5 L1 9" stroke="#fff" fill="none" stroke-width="1"/></svg>
      100% <div class="battery"><span></span></div>
    </div>
  </div>

  <section class="appointments">
    <header class="app-header">
      <svg class="menu-btn" width="24" height="20" viewBox="0 0 24 20"><rect y="1" width="24" height="3" fill="#fff"/><rect y="8.5" width="24" height="3" fill="#fff"/><rect y="16" width="24" height="3" fill="#fff"/></svg>
      Appointments
      <svg class="add-btn" width="28" height="28" viewBox="0 0 28 28"><circle cx="14" cy="14" r="13" fill="#fff"/><path d="M14 7 V21 M7 14 H21" stroke="var(--teal)" stroke-width="2.6"/></svg>
    </header>
    <div class="consultant-filter">All Consultants <span class="caret"></span></div>

    <span class="time-label" style="top:131px">08:00 AM</span>
    <article class="appt-card" style="top:131px">
      <div class="avatar" role="img" aria-label="Client photo" style="background:#9a5a45"></div>
      <h3 class="person-name">Delphine Ruth Carver</h3>
      <p class="services">Haircut, Pedicure, Manicure</p>
      <p class="consultant"><span class="dot ok"><svg width="10" height="11" viewBox="0 0 10 11"><circle cx="5" cy="3" r="2.5" fill="#fff"/><path d="M0.5 11 A4.5 4.5 0 0 1 9.5 11 Z" fill="#fff"/></svg></span>Theo &amp; Lina</p>
    </article>
    <article class="appt-card" style="top:247px">
      <div class="avatar" role="img" aria-label="Client photo" style="background:#5a4a44"></div>
      <h3 class="person-name">Owen Marsh</h3>
      <p class="services">Haircut, Massage</p>
      <p class="consultant"><span class="dot wait"><svg width="10" height="11" viewBox="0 0 10 11"><circle cx="5" cy="3" r="2.5" fill="#fff"/><path d="M0.5 11 A4.5 4.5 0 0 1 9.5 11 Z" fill="#fff"/></svg></span>Sam &amp; Nico</p>
    </article>
    <article class="appt-card" style="top:363px">
      <div class="avatar" role="img" aria-label="Client photo" style="background:#c9a57c"></div>
      <h3 class="person-name">Priya Halvorsen</h3>
      <p class="services">Haircut, Pedicure, Manicure</p>
      <p class="consultant"><span class="dot late"><svg width="10" height="11" viewBox="0 0 10 11"><circle cx="5" cy="3" r="2.5" fill="#fff"/><path d="M0.5 11 A4.5 4.5 0 0 1 9.5 11 Z" fill="#fff"/></svg></span>Sam &amp; Nico</p>
    </article>

    <span class="time-label" style="top:501px">08:30 AM</span>
    <article class="appt-card" style="top:501px">
      <div class="avatar" role="img" aria-label="Client photo" style="background:#6b5446"></div>
      <h3 class="person-name">Tobias Wren</h3>
      <p class="services">Haircut, Hairstyling, Massage</p>
      <p class="consultant"><span class="dot ok"><svg width="10" height="11" viewBox="0 0 10 11"><circle cx="5" cy="3" r="2.5" fill="#fff"/><path d="M0.5 11 A4.5 4.5 0 0 1 9.5 11 Z" fill="#fff"/></svg></span>Theo &amp; Lina</p>
    </article>

    <span class="time-label" style="top:641px">09:00 AM</span>
    <article class="appt-card" style="top:641px">
      <div class="avatar" role="img" aria-label="Client photo" style="background:#5c4438"></div>
      <h3 class="person-name">Maren Ostby</h3>
      <p class="services">Haircut, Pedicure, Manicure</p>
      <p class="consultant"><span class="dot wait"><svg width="10" height="11" viewBox="0 0 10 11"><circle cx="5" cy="3" r="2.5" fill="#fff"/><path d="M0.5 11 A4.5 4.5 0 0 1 9.5 11 Z" fill="#fff"/></svg></span>Ravi &amp; Dana</p>
    </article>
    <article class="appt-card" style="top:757px">
      <div class="avatar" role="img" aria-label="Client photo" style="background:#4e4040"></div>
      <h3 class="person-name">Felix Durand</h3>
      <p class="services">Haircut, Massage</p>
      <p class="consultant"><span class="dot late"><svg width="10" height="11" viewBox="0 0 10 11"><circle cx="5" cy="3" r="2.5" fill="#fff"/><path d="M0.5 11 A4.5 4.5 0 0 1 9.5 11 Z" fill="#fff"/></svg></span>Janice</p>
    </article>
  </section>

  <section class="check-in">
    <header class="check-header">Check In</header>
    <div class="search-bar">
      <svg width="18" height="18" viewBox="0 0 18 18"><circle cx="7.5" cy="7.5" r="6" stroke="#fff" stroke-width="1.6" fill="none"/><path d="M12 12 L17 17" stroke="#fff" stroke-width="1.6"/></svg>
      Search Customer
    </div>

    <article class="checkin-card" style="top:128px">
      <div class="avatar" role="img" aria-label="Client photo" style="background:#6e4b3c"></div>
      <h3 class="person-name">Serena Vale</h3>
      <p class="services">Haircut, Hairstyling, Pedicure, Manicure</p>
      <p class="consultant"><span class="dot ok"><svg width="10" height="11" viewBox="0 0 10 11"><circle cx="5" cy="3" r="2.5" fill="#fff"/><path d="M0.5 11 A4.5 4.5 0 0 1 9.5 11 Z" fill="#fff"/></svg></span>Kat &amp; Kate</p>
    </article>
    <article class="checkin-card" style="top:261px">
      <div class="avatar" role="img" aria-label="Client photo" style="background:#4f5560"></div>
      <h3 class="person-name">Leon Ashby</h3>
      <p class="services">Haircut, Massage</p>
      <p class="consultant"><span class="dot ok"><svg width="10" height="11" viewBox="0 0 10 11"><circle cx="5" cy="3" r="2.5" fill="#fff"/><path d="M0.5 11 A4.5 4.5 0 0 1 9.5 11 Z" fill="#fff"/></svg></span>Mandy</p>
    </article>
    <article class="checkin-card" style="top:394px">
      <div class="avatar" role="img" aria-label="Client photo" style="background:#3a3a3e"></div>
      <h3 class="person-name">Gideon Marlow</h3>
      <p class="services">Haircut, Massage</p>
      <p class="consultant"><span class="dot ok"><svg width="10" height="11" viewBox="0 0 10 11"><circle cx="5" cy="3" r="2.5" fill="#fff"/><path d="M0.5 11 A4.5 4.5 0 0 1 9.5 11 Z" fill="#fff"/></svg></span>Cheska</p>
    </article>
  </section>
</main>
</body>
</html>
```